Junk Removal - Customers that are moving

junk collection business we want to gear this mailing to people who are moving and may need help in cleaning out the house for the open house or when the final move is near. Want to sound helpful and show it easier for us to do all the work

Target Market(s)

People Moving

Industry/Entity Type

House

Colors
3277b5
33a6d7

Requirements
Must have
• See attachment

```html
<!DOCTYPE html>
<html lang="en">
<head>
<meta charset="utf-8">
<title>1-855-TIDYHAUL Moving Mailer</title>
<link href="https://fonts.googleapis.com/css2?family=Open+Sans:wght@400;600;700;800&family=Roboto+Condensed:wght@700&display=swap" rel="stylesheet">
<style>
  :root{
    --blue:#3277b5;
    --sky:#33a6d7;
    --band:#1f5ca8;
    --ink:#2b2b2b;
    --grey:#8d8f92;
    --pill:#4a4c50;
    --page:#e4e4e4;
    --panel:#e3e4e6;
  }
  *{box-sizing:border-box;margin:0;padding:0}
  html,body{width:837px;height:1200px;overflow:hidden}
  body{background:var(--page);font-family:"Open Sans",Arial,sans-serif;color:var(--ink);position:relative}
  .card{position:absolute;left:68px;width:700px;background:#fff;overflow:hidden;box-shadow:0 2px 6px rgba(0,0,0,.18)}
  .card--front{top:40px;height:538px}
  .card--back{top:622px;height:540px}

  /* front */
  .tagline{position:absolute;left:34px;top:66px;font-family:"Roboto Condensed",Arial,sans-serif;font-weight:700;font-size:23px;color:#9a9c9f;letter-spacing:.2px;white-space:nowrap}
  .tagline .phone{color:#1d1d1d}
  .brand-name{position:absolute;left:30px;top:100px;font-family:"Open Sans",Arial,sans-serif;font-weight:800;font-size:62px;color:var(--blue);letter-spacing:-2px;line-height:1;white-space:nowrap}
  .mascot{position:absolute;left:520px;top:8px;width:160px;height:206px;border-radius:8px;background:linear-gradient(180deg,#dce9f6 0%,#b9cfe6 60%,#d9dcdf 100%)}
  .hero-photo{position:absolute;left:257px;top:223px;width:443px;height:282px;background:linear-gradient(135deg,#f3f5f7 0%,#dfe6ec 45%,#c9b08f 80%,#e7e9eb 100%)}
  .letter{position:absolute;left:34px;top:236px;width:212px;font-size:13.5px;line-height:1.5}
  .letter p{margin-bottom:12px}
  .coupon{position:absolute;left:34px;top:393px;width:230px;font-weight:800;font-size:20.5px;line-height:1.2;color:var(--blue)}
  .web-pill{position:absolute;left:0;top:476px;width:272px;height:29px;background:var(--pill);border-top-right-radius:22px;color:#fff;font-weight:700;font-size:15px;letter-spacing:.5px;line-height:29px;padding-left:52px}
  .band{position:absolute;left:0;width:100%;background:var(--band);color:#fff;font-weight:700;text-align:center}
  .card--front .band{top:505px;height:33px;line-height:33px;font-size:17px}

  /* back */
  .top-rule{position:absolute;left:0;top:0;width:100%;height:9px;background:var(--band)}
  .benefits{position:absolute;left:22px;top:28px;width:445px;list-style:none;font-size:12.8px;line-height:1.5;text-align:justify}
  .benefits li{position:relative;padding-left:22px;margin-bottom:8px}
  .benefits svg{position:absolute;left:0;top:4px;width:12px;height:12px}
  .closing{position:absolute;left:22px;top:386px;width:445px;font-size:12.8px;line-height:1.5}
  .closing p{margin-bottom:10px}
  .closing .sign{font-weight:700;margin-top:14px}
  .mail-panel{position:absolute;left:482px;top:30px;width:194px;height:468px;background:var(--panel);border-radius:10px}
  .stamp{position:absolute;left:4px;top:10px;width:143px;height:120px;background:#b9babc}
  .card--back .band{top:510px;height:30px;line-height:30px;font-size:17px}
</style>
</head>
<body>

<section class="card card--front">
  <div class="tagline">SAFE, SECURE JUNK REMOVAL <span class="phone">1-855-555-0147</span></div>
  <div class="brand-name">1-855-TIDYHAUL</div>
  <div class="mascot" role="img" aria-label="Cartoon worker in a cap leaning on a broom beside a trash can"></div>

  <div class="hero-photo" role="img" aria-label="Photo of two young men carrying a white sofa and moving boxes in a bright room"></div>

  <div class="letter">
    <p>Dear Home owner,</p>
    <p>Congratulations on your upcoming move!</p>
    <p>We know how exciting and stressful moving your family and all your belongings can be.</p>
  </div>
  <div class="coupon">$25 DISCOUNT COUPON off any junk removal job!</div>

  <div class="web-pill">www.1855tidyhaul.com</div>
  <div class="band">Let 1-855-TIDYHAUL help take some of the stress out of your move!</div>
</section>

<section class="card card--back">
  <div class="top-rule"></div>

  <ul class="benefits">
    <li><svg viewBox="0 0 12 12"><circle cx="6" cy="6" r="6" fill="#3277b5"/><path d="M3.2 6.2l1.9 1.9 3.7-4" fill="none" stroke="#fff" stroke-width="1.6"/></svg>No need to collect and remove unwanted items from the property; just point it out and we do all the work!</li>
    <li><svg viewBox="0 0 12 12"><circle cx="6" cy="6" r="6" fill="#3277b5"/><path d="M3.2 6.2l1.9 1.9 3.7-4" fill="none" stroke="#fff" stroke-width="1.6"/></svg>No storage units or dumpsters to deal with, no physical work to worry about.</li>
    <li><svg viewBox="0 0 12 12"><circle cx="6" cy="6" r="6" fill="#3277b5"/><path d="M3.2 6.2l1.9 1.9 3.7-4" fill="none" stroke="#fff" stroke-width="1.6"/></svg>We leave the areas from which we remove your unwanted “junk” “broom clean”.</li>
    <li><svg viewBox="0 0 12 12"><circle cx="6" cy="6" r="6" fill="#3277b5"/><path d="M3.2 6.2l1.9 1.9 3.7-4" fill="none" stroke="#fff" stroke-width="1.6"/></svg>Our up front price is not an estimate; the price we quote is the price you pay!</li>
    <li><svg viewBox="0 0 12 12"><circle cx="6" cy="6" r="6" fill="#3277b5"/><path d="M3.2 6.2l1.9 1.9 3.7-4" fill="none" stroke="#fff" stroke-width="1.6"/></svg>We responsibly dispose of or recycle all items we remove.</li>
    <li><svg viewBox="0 0 12 12"><circle cx="6" cy="6" r="6" fill="#3277b5"/><path d="M3.2 6.2l1.9 1.9 3.7-4" fill="none" stroke="#fff" stroke-width="1.6"/></svg>Our services are ideal for both the initial cleanout of your for your open house or final cleanout days before moving <b>1-855TIDYHAUL (1-855-555-0147)</b> is the one number to call.</li>
    <li><svg viewBox="0 0 12 12"><circle cx="6" cy="6" r="6" fill="#3277b5"/><path d="M3.2 6.2l1.9 1.9 3.7-4" fill="none" stroke="#fff" stroke-width="1.6"/></svg>We remove all sorts of clutter including: Unwanted furniture, books, clothing, appliances, electronics, construction debris, carpeting, tile, mattresses, tires and much more!</li>
  </ul>

  <div class="closing">
    <p>Visit our website www.1855TIDYHAUL.com or give us a call for more information.</p>
    <p>Wishing you the best of luck in your new home!</p>
    <p class="sign">The 1-855 TIDYHAUL Team</p>
  </div>

  <div class="mail-panel"><div class="stamp"></div></div>

  <div class="band">More than 75 years of family business behind all our work</div>
</section>

</body>
</html>
```